Business cards for 3 Realtors at one brokerage

We will need a business card template that can be projected on 3 business cards. Summit Crest Property & Holdings Corp. has 3 realtors on staff Dale, Owen, and Brady. We all want a business card that shows our new logo and information. I will attach many versions of our Logo as well as head shots for each realtor (Owen- Long hair, youngest. Brady- Suit jacket, parted hair cut. Dale- Angled Pose, Shirt and Tie.) I have attached our information below.

Dale Forsythe
801-555-0147
dale@summitcresthomes.com
Principal Broker

Brady Tidwell
801-555-0192
brady@summitcresthomes.com
Real Estate Agent

Owen Tidwell
801-555-0163
owen@summitcresthomes.com
Real Estate Agent

Summit Crest Property & Holdings Corp.
SummitCrestHomes.com
2918 W 8650 Suite 204-117, Alder Bend, UT 84990

Please feel free to reach out with any questions, comments, or concerns.

```html
<!DOCTYPE html>
<html lang="en">
<head>
<meta charset="utf-8">
<title>Summit Crest Property &amp; Holdings Corp. – Business Cards</title>
<link rel="stylesheet" href="https://fonts.googleapis.com/css2?family=Poppins:wght@400;500;600&display=swap">
<style>
  :root {
    --page-bg: #dee4ea;
    --brand-blue: #36a9f7;
    --brand-grey: #6f6f6f;
    --band-grey: #757575;
    --text-dark: #4a4a4a;
    --white: #ffffff;
    --faint-ring: #ececec;
    --photo-top: #b89a80;
    --photo-bottom: #e9eef4;
  }
  * { box-sizing: border-box; margin: 0; padding: 0; }
  html, body { width: 1200px; height: 806px; overflow: hidden; }
  body {
    background: var(--page-bg);
    font-family: "Poppins", sans-serif;
    position: relative;
  }
  .card {
    position: absolute;
    top: 301px;
    width: 330px;
    height: 204px;
    overflow: hidden;
    box-shadow: 0 1px 2px rgba(0,0,0,0.25);
  }
  .card-front { left: 255px; background: var(--white); }
  .card-back { left: 615px; background: var(--brand-blue); }

  /* front */
  .front-ring {
    position: absolute; left: 145px; top: -8px;
    width: 190px; height: 190px; border-radius: 50%;
    border: 12px solid var(--faint-ring);
  }
  .brand-front {
    position: absolute; left: 0; top: 18px; width: 164px;
    text-align: center; color: var(--brand-grey); font-weight: 500;
  }
  .brand-dot {
    display: block; margin: 0 auto 8px;
    width: 40px; height: 40px; border-radius: 50%;
    border: 3px solid var(--brand-blue);
  }
  .brand-front .brand-name { font-size: 12.5px; line-height: 1; letter-spacing: 0.2px; }
  .brand-front .brand-sub { font-size: 5px; letter-spacing: 1.3px; margin-top: 3px; }

  .name-band {
    position: absolute; left: 0; top: 95px; width: 330px; height: 42px;
    background: var(--brand-blue);
  }
  .name-band-grey {
    position: absolute; right: 0; top: 0; width: 60px; height: 100%;
    background: var(--band-grey);
  }
  .agent-name {
    position: absolute; left: 27px; top: 105px;
    color: var(--white); font-weight: 500; font-size: 11.5px; line-height: 1;
  }
  .agent-title {
    position: absolute; left: 27px; top: 119px;
    color: var(--white); font-weight: 500; font-size: 9.5px; line-height: 1;
  }
  .contact-list {
    position: absolute; left: 27px; top: 145px; list-style: none;
    color: var(--text-dark); font-size: 10px; line-height: 12.6px;
  }
  .contact-list li { display: flex; align-items: center; gap: 3px; }
  .contact-list svg { width: 10px; height: 10px; flex: none; }
  .contact-list .accent { color: var(--brand-blue); }
  .headshot {
    position: absolute; left: 190px; top: 10px; width: 140px; height: 194px;
    background: linear-gradient(180deg, var(--photo-top) 0%, var(--photo-top) 42%, var(--photo-bottom) 50%, var(--photo-bottom) 100%);
    clip-path: polygon(32% 0, 64% 0, 78% 12%, 78% 38%, 66% 48%, 92% 58%, 100% 66%, 100% 100%, 0 100%, 2% 72%, 10% 60%, 34% 48%, 22% 38%, 20% 12%);
  }

  /* back */
  .back-ring {
    position: absolute; left: 178px; top: 2px;
    width: 200px; height: 200px; border-radius: 50%;
    border: 12px solid rgba(255,255,255,0.08);
  }
  .brand-back {
    position: absolute; left: 0; top: 35px; width: 100%;
    text-align: center; color: var(--white); font-weight: 500;
  }
  .brand-back .brand-dot { width: 60px; height: 60px; border-color: var(--white); border-width: 3px; margin-bottom: 8px; }
  .brand-back .brand-name { font-size: 17px; line-height: 1; letter-spacing: 0.3px; }
  .brand-back .brand-sub { font-size: 7px; letter-spacing: 2px; margin-top: 4px; }
  .pin-divider {
    position: absolute; left: 123px; top: 140px; width: 84px; height: 14px;
  }
  .back-address {
    position: absolute; left: 0; top: 157px; width: 100%;
    text-align: center; color: var(--white); font-size: 9.8px; font-weight: 500; line-height: 12.5px;
  }
  .back-address .web { font-weight: 400; }
</style>
</head>
<body>
  <section class="card card-front">
    <div class="front-ring"></div>
    <div class="name-band"><div class="name-band-grey"></div></div>
    <div class="headshot" role="img" aria-label="Headshot of Owen Tidwell in a white shirt"></div>
    <div class="brand-front">
      <span class="brand-dot"></span>
      <div class="brand-name">SUMMIT CREST</div>
      <div class="brand-sub">PROPERTY &amp; HOLDINGS CORP.</div>
    </div>
    <div class="agent-name">OWEN TIDWELL</div>
    <div class="agent-title">Real Estate Agent</div>
    <ul class="contact-list">
      <li>
        <svg viewBox="0 0 10 10"><circle cx="5" cy="5" r="5" fill="var(--brand-blue)"/><path d="M3.2 2.6l1 1-.5.6c.4.8.9 1.3 1.6 1.6l.6-.5 1 1-.6.8c-1.9-.3-3.6-2-3.9-3.9z" fill="#fff"/></svg>
        801-555-0163
      </li>
      <li>
        <svg viewBox="0 0 10 10"><circle cx="5" cy="5" r="5" fill="var(--brand-blue)"/><rect x="2.6" y="3.3" width="4.8" height="3.4" fill="#fff"/><path d="M2.6 3.3L5 5.2 7.4 3.3" stroke="var(--brand-blue)" stroke-width="0.6" fill="none"/></svg>
        owen@summitcresthomes.com
      </li>
      <li>
        <svg viewBox="0 0 10 10"><circle cx="5" cy="5" r="5" fill="var(--brand-blue)"/><circle cx="5" cy="5" r="2.6" fill="none" stroke="#fff" stroke-width="0.6"/><path d="M2.4 5h5.2M5 2.4v5.2" stroke="#fff" stroke-width="0.6"/></svg>
        <span>www.<span class="accent">SummitCrestHomes</span>.com</span>
      </li>
    </ul>
  </section>

  <section class="card card-back">
    <div class="back-ring"></div>
    <div class="brand-back">
      <span class="brand-dot"></span>
      <div class="brand-name">SUMMIT CREST</div>
      <div class="brand-sub">PROPERTY &amp; HOLDINGS CORP.</div>
    </div>
    <svg class="pin-divider" viewBox="0 0 84 14">
      <line x1="0" y1="7" x2="28" y2="7" stroke="#fff" stroke-width="0.8"/>
      <line x1="56" y1="7" x2="84" y2="7" stroke="#fff" stroke-width="0.8"/>
      <circle cx="42" cy="7" r="6.5" fill="#fff"/>
      <path d="M42 3.6a2.4 2.4 0 0 1 2.4 2.4c0 1.7-2.4 4.2-2.4 4.2s-2.4-2.5-2.4-4.2A2.4 2.4 0 0 1 42 3.6z" fill="var(--brand-blue)"/>
      <circle cx="42" cy="6" r="0.9" fill="#fff"/>
    </svg>
    <div class="back-address">
      <div>2918 W 8650 Suite 204-117, Alder Bend, UT 84990</div>
      <div class="web">www.SummitCrestHomes.com</div>
    </div>
  </section>
</body>
</html>
```